New residential property management company

I have a lot of name recognition in our smaller town due to owning a construction company here. I have now started a residential property management company representing landlords and tenants. Just trying to get my name out there and get some rentals to manage!

```html
<!DOCTYPE html>
<html lang="en">
<head>
<meta charset="UTF-8">
<title>Harlow Property Management – Postcard</title>
<link rel="stylesheet" href="https://fonts.googleapis.com/css2?family=Montserrat:wght@500;600;700;800&family=Open+Sans:wght@400;600&display=swap">
<style>
  :root {
    --red: #8a0a0a;
    --blue: #0a72bb;
    --ink: #1c1c1c;
    --dark: #2a2a2a;
    --paper: #efefef;
    --white: #ffffff;
    --stamp: #e6e6e6;
    --rule: #9a9a9a;
  }
  * { box-sizing: border-box; margin: 0; padding: 0; }
  html, body { width: 900px; height: 1200px; overflow: hidden; background: var(--white); }
  body { position: relative; font-family: "Montserrat", sans-serif; color: var(--ink); }

  .card {
    position: absolute; left: 113px; width: 672px; height: 480px;
    overflow: hidden; box-shadow: 0 10px 28px rgba(0,0,0,.35);
  }
  .card--front { top: 92px; }
  .card--back { top: 635px; background: var(--paper); }

  .abs { position: absolute; }

  /* front */
  .hero-photo {
    left: 0; top: 0; width: 672px; height: 480px;
    background:
      linear-gradient(90deg, rgba(230,238,243,0) 55%, rgba(40,55,85,.85) 78%, #1f2b44 100%),
      linear-gradient(180deg, #cfdde5 0%, #eef2f4 55%, #dfe7ec 100%);
  }
  .brand { display: flex; align-items: center; gap: 12px; }
  .brand__mark { background: var(--ink); flex: none; }
  .brand__name { font-weight: 600; color: var(--ink); line-height: 1; letter-spacing: .01em; white-space: nowrap; }
  .brand__tag { font-weight: 700; color: var(--ink); letter-spacing: .2em; line-height: 1; white-space: nowrap; }

  .front-brand { left: 53px; top: 48px; }
  .front-brand .brand__mark { width: 52px; height: 58px; }
  .front-brand .brand__name { font-size: 46px; }
  .front-brand .brand__tag { font-size: 7px; margin-top: 7px; margin-left: 8px; }

  .headline { left: 50px; top: 138px; font-size: 40px; line-height: 46px; }
  .headline span { display: block; }
  .headline .strong { font-weight: 800; color: var(--red); }
  .headline .light { font-weight: 500; color: var(--ink); }

  .bands { left: 0; top: 0; }
  .name-pill {
    left: 51px; top: 344px; width: 200px; height: 41px; border-radius: 21px 0 0 21px;
    background: var(--blue); color: var(--white); font-weight: 700; font-size: 26px;
    padding-left: 22px; line-height: 41px;
  }
  .agent-photo {
    left: 205px; top: 323px; width: 140px; height: 140px; border-radius: 50%;
    border: 6px solid #9fa5aa;
    background: linear-gradient(160deg, #e9eef1 0%, #c9d2d8 50%, #2b2f36 100%);
  }
  .call-now { left: 75px; top: 428px; color: var(--white); font-weight: 700; font-size: 20px; letter-spacing: .01em; }
  .phone-pill {
    left: 344px; top: 406px; width: 279px; height: 42px; border-radius: 0 21px 21px 0;
    background: var(--white); overflow: hidden;
  }
  .phone-pill__lead { left: 0; top: 0; width: 40px; height: 42px; background: var(--blue); }
  .phone-pill__icon { left: 2px; top: 2px; }
  .phone-pill__number { left: 51px; top: 0; line-height: 42px; font-size: 31px; font-weight: 700; color: var(--red); letter-spacing: .01em; }

  /* back */
  .back-shapes { left: 0; top: 0; }
  .pitch { left: 39px; top: 33px; font-weight: 800; font-size: 20px; line-height: 25px; }
  .pitch .red { color: var(--red); display: block; }
  .pitch .blue { color: var(--blue); display: block; }

  .section-tag {
    width: 154px; height: 23px; background: var(--red); color: var(--white);
    font-weight: 700; font-size: 16px; line-height: 23px; text-align: center;
  }
  .tag-who { left: 40px; top: 119px; }
  .tag-what { left: 40px; top: 227px; }
  .copy {
    left: 40px; width: 300px; font-family: "Open Sans", sans-serif; font-size: 9.6px;
    line-height: 13.7px; color: var(--ink);
  }
  .copy-who { top: 147px; }
  .copy-what { top: 255px; }

  .contact-box { left: 40px; top: 365px; width: 292px; height: 87px; background: var(--blue); }
  .tag-contact { left: 40px; top: 354px; font-size: 18px; height: 24px; line-height: 24px; }
  .contact-line { color: var(--white); font-size: 11px; font-weight: 500; display: flex; align-items: center; gap: 4px; }
  .contact-address { left: 57px; top: 389px; line-height: 13px; }
  .contact-address .indent { padding-left: 10px; display: block; }
  .contact-mail { left: 57px; top: 422px; }
  .contact-phone { left: 195px; top: 422px; }

  .back-brand { left: 400px; top: 41px; gap: 7px; }
  .back-brand .brand__mark { width: 26px; height: 30px; }
  .back-brand .brand__name { font-size: 21px; }
  .back-brand .brand__tag { font-size: 3.6px; margin-top: 3px; margin-left: 4px; letter-spacing: .15em; }

  .stamp { left: 541px; top: 39px; width: 92px; height: 92px; background: var(--stamp); border: 1px solid #b4b4b4; }
  .address-rule { left: 441px; width: 192px; height: 1px; background: var(--rule); }
</style>
</head>
<body>

<section class="card card--front" aria-label="Postcard front">
  <div class="abs hero-photo" role="img" aria-label="Photo of a businessman in a dark suit holding a white model house over a soft city backdrop"></div>

  <div class="abs brand front-brand">
    <div class="brand__mark"></div>
    <div>
      <div class="brand__name">HARLOW</div>
      <div class="brand__tag">PROPERTY MANAGEMENT LLC.</div>
    </div>
  </div>

  <h1 class="abs headline">
    <span class="strong">RESIDENTIAL</span>
    <span class="light">PROPERTY</span>
    <span class="strong">MANAGEMENT</span>
    <span class="light">COMPANY</span>
  </h1>

  <svg class="abs bands" width="672" height="480" viewBox="0 0 672 480" aria-hidden="true">
    <polygon points="0,360 545,360 0,420" fill="var(--red)"/>
    <polygon points="0,423 672,349 672,480 0,480" fill="var(--dark)"/>
    <line x1="0" y1="421" x2="672" y2="347" stroke="var(--white)" stroke-width="4"/>
  </svg>

  <div class="abs name-pill">John Doe</div>
  <div class="abs agent-photo" role="img" aria-label="Portrait photo of the agent seated at a desk with a laptop"></div>

  <div class="abs call-now">CALL NOW</div>

  <div class="abs phone-pill">
    <div class="abs phone-pill__lead"></div>
    <svg class="abs phone-pill__icon" width="38" height="38" viewBox="0 0 38 38" aria-hidden="true">
      <circle cx="19" cy="19" r="17" fill="var(--blue)" stroke="var(--white)" stroke-width="2.5"/>
      <path d="M13 11c1-1 2.5-1 3 .3l1.4 3c.4.8 0 1.6-.6 2l-1.3.9c.8 2.3 2.5 4.2 4.6 5.4l1-1.2c.5-.6 1.4-.8 2.1-.3l2.8 1.700c1.1.7 1 2.1 0 3l-1.3 1.1c-1.3 1.1-3.2 1.2-4.7.4-4.2-2.2-7.4-6-8.7-10.6-.4-1.6 0-3.3 1.1-4.4z" fill="var(--white)"/>
    </svg>
    <div class="abs phone-pill__number">0123 456 789</div>
  </div>
</section>

<section class="card card--back" aria-label="Postcard back">
  <svg class="abs back-shapes" width="672" height="480" viewBox="0 0 672 480" aria-hidden="true">
    <polygon points="372,0 672,0 672,480 438,480" fill="var(--white)"/>
    <polygon points="319,0 372,0 396,294" fill="var(--blue)"/>
  </svg>

  <h2 class="abs pitch">
    <span class="red">PROFESSIONAL</span>
    <span class="blue">PROPERTY MANAGEMENT</span>
    <span class="red">YOU CAN TRUST.</span>
  </h2>

  <div class="abs section-tag tag-who">WHO WE ARE</div>
  <p class="abs copy copy-who">We are your local, worry-free property management company. It doesn’t matter if you are a board member or homeowner, or if you’re an investor that owns commercial, vacation or residential rental property. We are here to support you with all your property management needs.</p>

  <div class="abs section-tag tag-what">WHAT WE DO</div>
  <p class="abs copy copy-what">We protect your investments, build value in our communities, and provide superior service and support. Our unique strategy, focused on all four pillars of property management, allows us an unparalleled advantage in the industry. When you partner with HPM you can be sure that you’re going to have the best property management available.</p>

  <div class="abs contact-box"></div>
  <div class="abs section-tag tag-contact">CONTACT US</div>

  <div class="abs contact-line contact-address">
    <div>
      <span>
        <svg width="7" height="9" viewBox="0 0 7 9" aria-hidden="true"><circle cx="3.5" cy="3" r="2.2" fill="none" stroke="#fff" stroke-width="1"/><line x1="3.5" y1="5.2" x2="3.5" y2="8.5" stroke="#fff" stroke-width="1"/></svg>
        address line 1, address line 1
      </span>
      <span class="indent">address line 2</span>
    </div>
  </div>
  <div class="abs contact-line contact-mail">
    <svg width="9" height="7" viewBox="0 0 9 7" aria-hidden="true"><rect x=".5" y=".5" width="8" height="6" fill="none" stroke="#fff" stroke-width="1"/><polyline points=".5,.5 4.5,4 8.5,.5" fill="none" stroke="#fff" stroke-width="1"/></svg>
    info@yourmail.com
  </div>
  <div class="abs contact-line contact-phone">
    <svg width="9" height="9" viewBox="0 0 9 9" aria-hidden="true"><circle cx="4.5" cy="4.5" r="4" fill="none" stroke="#fff" stroke-width="1"/><path d="M3.2 2.4l.7 1.1-.5.5c.3.6.7 1 1.3 1.3l.5-.5 1.1.7-.4.8c-1.6-.2-3.1-1.700-3.3-3.3z" fill="#fff"/></svg>
    0123 456 789
  </div>

  <div class="abs brand back-brand">
    <div class="brand__mark"></div>
    <div>
      <div class="brand__name">HARLOW</div>
      <div class="brand__tag">PROPERTY MANAGEMENT LLC.</div>
    </div>
  </div>

  <div class="abs stamp"></div>
  <div class="abs address-rule" style="top:279px"></div>
  <div class="abs address-rule" style="top:320px"></div>
  <div class="abs address-rule" style="top:362px"></div>
</section>

</body>
</html>
```